Business Card Design

we are a brand new cable TV network devoted to self improvement and leading a better life called FLOURIVO TV.I have a logo. We have 3 executives that need cards.I want it to be a heavy stock card: professional but showing our creative nature

Industry/Entity Type

Business

Contact Information for Business Card

CLAUDIA SAENZ AMLIECEO350 San Juan DrPonte Vedra Beach FL 32082904-473-5953

```html
<!DOCTYPE html>
<html lang="en">
<head>
<meta charset="UTF-8">
<title>Flourivo TV – Business Card</title>
<link rel="stylesheet" href="https://fonts.googleapis.com/css2?family=Poppins:wght@600&family=Roboto:wght@400;500&display=swap">
<style>
  :root {
    --backdrop: #2b2b2b;
    --red-deep: #9c1e26;
    --red-mid: #c8202b;
    --red-glow: #d8323c;
    --white: #ffffff;
    --ink: #2a2a2a;
  }
  * { margin: 0; padding: 0; box-sizing: border-box; }
  html, body {
    width: 1200px;
    height: 750px;
    overflow: hidden;
    background: var(--backdrop);
  }
  .canvas {
    width: 1200px;
    height: 750px;
    display: flex;
    flex-direction: column;
    align-items: center;
    justify-content: center;
    gap: 40px;
  }
  .card {
    position: relative;
    width: 520px;
    height: 297px;
    overflow: hidden;
    box-shadow: 0 10px 30px rgba(0,0,0,0.5);
  }
  .card-front {
    background:
      radial-gradient(ellipse at 45% 55%, var(--red-glow) 0%, var(--red-mid) 40%, var(--red-deep) 100%);
    display: flex;
    align-items: center;
    justify-content: center;
  }
  .wordmark {
    font-family: "Poppins", sans-serif;
    font-weight: 600;
    font-size: 48px;
    letter-spacing: 0.5px;
    line-height: 1;
  }
  .card-front .wordmark { color: var(--white); }
  .card-back { background: var(--white); }
  .back-shape {
    position: absolute;
    inset: 0;
  }
  .back-logo {
    position: absolute;
    left: 0;
    top: 0;
    width: 250px;
    height: 297px;
    display: flex;
    align-items: center;
    justify-content: center;
    gap: 8px;
  }
  .back-logo .mark-square {
    width: 14px;
    height: 14px;
    background: var(--red-mid);
  }
  .back-logo .wordmark {
    color: var(--ink);
    font-size: 30px;
  }
  .contact {
    position: absolute;
    left: 290px;
    top: 78px;
    color: var(--white);
    font-family: "Roboto", sans-serif;
  }
  .contact-name {
    font-weight: 500;
    font-size: 14px;
    letter-spacing: 0.3px;
    text-transform: uppercase;
  }
  .contact-title {
    font-size: 13px;
    margin-top: 6px;
    padding-left: 14px;
  }
  .contact-address {
    font-size: 13px;
    line-height: 1.45;
    margin-top: 42px;
    padding-left: 40px;
  }
  .contact-phone {
    display: flex;
    align-items: center;
    gap: 6px;
    font-size: 13px;
    padding-left: 40px;
    margin-top: 2px;
  }
  .contact-phone svg { width: 13px; height: 13px; }
</style>
</head>
<body>
  <main class="canvas">
    <section class="card card-front" aria-label="Card front">
      <span class="wordmark">Flourivo TV</span>
    </section>

    <section class="card card-back" aria-label="Card back">
      <svg class="back-shape" viewBox="0 0 520 297" aria-hidden="true">
        <defs>
          <radialGradient id="panelRed" cx="50%" cy="35%" r="75%">
            <stop offset="0%" stop-color="#d8323c"/>
            <stop offset="45%" stop-color="#c8202b"/>
            <stop offset="100%" stop-color="#9c1e26"/>
          </radialGradient>
        </defs>
        <path d="M258 0 H520 V297 H258 V108 L268 100 L258 92 Z" fill="url(#panelRed)"/>
        <path d="M250 0 V92 L260 100 L250 108 V297" fill="none" stroke="#c8202b" stroke-width="2"/>
      </svg>

      <div class="back-logo">
        <span class="mark-square"></span>
        <span class="wordmark">Flourivo TV</span>
      </div>

      <div class="contact">
        <p class="contact-name">Mirella Okafor Dunst</p>
        <p class="contact-title">CEO</p>
        <p class="contact-address">718 Harlow Creek Dr<br>Ponte Vedra Beach FL 32097</p>
        <p class="contact-phone">
          <svg viewBox="0 0 24 24" aria-hidden="true"><path fill="#ffffff" d="M6.6 10.8a15.1 15.1 0 0 0 6.6 6.6l2.2-2.2a1 1 0 0 1 1-.25 11.4 11.4 0 0 0 3.6.57 1 1 0 0 1 1 1V20a1 1 0 0 1-1 1A17 17 0 0 1 3 4a1 1 0 0 1 1-1h3.5a1 1 0 0 1 1 1c0 1.25.2 2.45.57 3.57a1 1 0 0 1-.25 1z"/></svg>
          904-618-2047
        </p>
      </div>
    </section>
  </main>
</body>
</html>
```